Amber Heron Fund Pitch Deck

This is a PowerPoint for use in investor presentations. The copy is written (although it may have small tweaks) and the designer will be responsible for creating a template and some graphical representations inside the presentation.

Note on the logo. Only the Amber Heron should be used, not the text.

```html
<!DOCTYPE html>
<html lang="en">
<head>
<meta charset="utf-8">
<title>Amber Heron Fund – Pitch Deck Slides</title>
<link href="https://fonts.googleapis.com/css2?family=Didact+Gothic&family=Nunito:wght@700;800&display=swap" rel="stylesheet">
<style>
  :root{
    --navy:#0f2160;
    --periwinkle:#6b8bc8;
    --slate:#5b6b9c;
    --ink:#1b1e28;
    --paper:#f5f6f8;
    --text-grey:#4a4f5c;
    --footer-grey:#a7adba;
    --white:#ffffff;
  }
  *{margin:0;padding:0;box-sizing:border-box}
  html,body{width:1200px;height:2194px;overflow:hidden;background:var(--white)}
  body{font-family:"Didact Gothic",sans-serif;position:relative}
  .slide{position:absolute;left:190px;width:816px;height:458px;overflow:hidden;box-shadow:0 8px 24px rgba(0,0,0,.35)}
  .heading{font-family:"Nunito",sans-serif;font-weight:800}
  .footer{position:absolute;top:424px;left:0;width:100%;height:16px;font-size:9.5px}
  .footer .brand{position:absolute;left:51px;top:0;font-size:11px;color:var(--white)}
  .footer .rights{position:absolute;left:253px;top:1px;color:var(--footer-grey)}
  .footer .page{position:absolute;left:713px;top:1px;color:var(--footer-grey);letter-spacing:.5px}

  /* Slide 1 – People */
  .people{top:93px;background:var(--navy)}
  .people .banner{position:absolute;left:0;top:0;width:100%;height:166px;background:linear-gradient(180deg,#c9ccd3 0%,#b5bfd6 45%,var(--periwinkle) 90%)}
  .people .title{position:absolute;left:42px;top:128px;font-size:23px;color:var(--white)}
  .member{position:absolute;top:186px;width:129px;color:var(--white)}
  .member .name{font-size:17px;line-height:20px}
  .member .role{font-size:10px;line-height:12px}
  .member .bio{margin-top:14px;font-size:10.4px;line-height:12.3px;text-align:justify}

  /* Slide 2 – Market */
  .market{top:607px;background:var(--paper)}
  .market .photo{position:absolute;inset:0}
  .market p{position:absolute;left:84px;width:300px;font-size:15.5px;line-height:18.3px;color:var(--white)}
  .market b{font-family:"Nunito",sans-serif;font-weight:700}
  .market .source{font-size:6.5px;line-height:8px;width:340px}
  .section-card{position:absolute;left:426px;top:87px;width:334px;height:283px;background:linear-gradient(180deg,#f2f3f5 0%,#c3c6cd 40%,#a2b1d3 70%,var(--periwinkle) 92%);box-shadow:0 6px 18px rgba(0,0,0,.35)}
  .section-card .num{position:absolute;right:16px;top:14px;font-size:27px;color:var(--periwinkle)}
  .section-card .label{position:absolute;left:40px;font-size:21px;color:var(--white)}
  .market .footer .rights{color:#c3c7d1}

  /* Slide 3 – Process */
  .process{top:1121px;background:var(--paper)}
  .process .photo{position:absolute;inset:0}
  .step{position:absolute;left:206px;width:44px;height:44px;border-radius:50%;background:radial-gradient(circle at 45% 25%,#e6e8ee 0%,#a6b3d6 45%,var(--periwinkle) 80%);box-shadow:0 3px 6px rgba(0,0,0,.3);color:var(--white);font-size:17px;text-align:center;line-height:44px}
  .step-text{position:absolute;font-size:12px;line-height:14.2px;color:var(--text-grey)}
  .step-text.left{right:628px;text-align:right;width:140px}
  .step-text.right{left:268px;width:150px}
  .process .section-card .label{top:250px}
  .process .section-card .desc{position:absolute;left:40px;top:282px;width:250px;font-size:11.6px;line-height:14.2px;color:var(--white)}
  .process .footer .brand{color:var(--periwinkle)}
  .process .footer .rights{color:#8d93a1}

  /* Slide 4 – Customers */
  .customers{top:1635px;background:var(--navy)}
  .customers .title{position:absolute;left:70px;top:38px;font-size:22px;color:var(--white)}
  .customers .skyline{position:absolute;left:0;top:107px;width:100%;height:244px;background:linear-gradient(180deg,#c8cad6 0%,#aeb4c8 55%,#8c95b4 100%)}
  .customers .frame{position:absolute;left:48px;top:91px;width:721px;height:314px;border:2px solid var(--white)}
  .customers .sub{position:absolute;left:70px;top:125px;font-size:23px;color:var(--periwinkle)}
  .stat{position:absolute;top:107px;width:161px;height:283px;background:linear-gradient(180deg,rgba(107,139,200,0) 0%,rgba(107,139,200,.55) 35%,var(--periwinkle) 70%);color:var(--white);text-align:center}
  .stat .value{margin-top:98px;font-size:48px;line-height:56px;letter-spacing:-1px}
  .stat .what{margin-top:14px;font-size:12.5px}
</style>
</head>
<body>

<section class="slide people">
  <div class="banner" role="img" aria-label="Photo of hands holding a pen over documents, fading to blue"></div>
  <h2 class="title heading">03 - The People</h2>
  <div class="member" style="left:28px">
    <div class="name">Glen Ostrander</div><div class="role">Managing Partner</div>
    <p class="bio">Lorem Ipsum is simply dummy text of the printing and typesetting industry. Lorem Ipsum has been the industry's standard dummy text ever since the 1500s, when an unknown printer took a galley of type and scrambled it to make a type specimen book.</p>
  </div>
  <div class="member" style="left:186px">
    <div class="name">Marcus Whitley</div><div class="role">Managing Partner</div>
    <p class="bio">Lorem Ipsum is simply dummy text of the printing and typesetting industry. Lorem Ipsum has been the industry's standard dummy text ever since the 1500s, when an unknown printer took a galley of type and scrambled it to make a type specimen book.</p>
  </div>
  <div class="member" style="left:344px">
    <div class="name">Owen Pratley</div><div class="role">Investment Committee</div>
    <p class="bio">Lorem Ipsum is simply dummy text of the printing and typesetting industry. Lorem Ipsum has been the industry's standard dummy text ever since the 1500s, when an unknown printer took a galley of type and scrambled it to make a type specimen book.</p>
  </div>
  <div class="member" style="left:502px">
    <div class="name">Simon Keller</div><div class="role">Dir of Credit Analytics.</div>
    <p class="bio">Lorem Ipsum is simply dummy text of the printing and typesetting industry. Lorem Ipsum has been the industry's standard dummy text ever since the 1500s, when an unknown printer took a galley of type and scrambled it to make a type specimen book.</p>
  </div>
  <div class="member" style="left:660px">
    <div class="name">Ray Dunmore</div><div class="role">Chief Operating Officer</div>
    <p class="bio">Lorem Ipsum is simply dummy text of the printing and typesetting industry. Lorem Ipsum has been the industry's standard dummy text ever since the 1500s, when an unknown printer took a galley of type and scrambled it to make a type specimen book.</p>
  </div>
  <footer class="footer"><span class="brand">Amber Heron</span><span class="rights">Not for distribution – All rights reserved © Amber Heron Fund</span><span class="page">page 15</span></footer>
</section>

<section class="slide market">
  <svg class="photo" width="816" height="458" viewBox="0 0 816 458" role="img" aria-label="Dark photo of a financial chart on a screen">
    <defs>
      <linearGradient id="darkPanel" x1="0" y1="0" x2="0" y2="1">
        <stop offset="0" stop-color="#5f6e9c"/>
        <stop offset=".45" stop-color="#3a4058"/>
        <stop offset="1" stop-color="#1a1c24"/>
      </linearGradient>
    </defs>
    <polygon points="0,0 442,0 714,458 0,458" fill="url(#darkPanel)"/>
  </svg>
  <p style="top:90px">The commercial lending market size was valued at <b>$8,823.53 billion in 2020</b>,</p>
  <p style="top:144px">and is <b>projected to reach $29,379.83 billion by 2030</b>, growing at a CAGR of 13.1% from 2021 to 2030. <sup style="font-size:6px">(*)</sup></p>
  <p style="top:234px">The credit cycle is entering into a period of rising interest rates and corresponding defaults. The fund seeks to take advantage of that emerging opportunity.</p>
  <p class="source" style="top:350px">(*) Source:<br>https://www.northfieldinsights.com/commercial-lending-market-A11617</p>
  <div class="section-card" role="img" aria-label="Faceted grey texture fading to blue">
    <span class="num heading">04</span>
    <span class="label heading" style="top:250px">The Market</span>
  </div>
  <footer class="footer"><span class="brand">Amber Heron</span><span class="rights">Not for distribution – All rights reserved © Amber Heron Fund</span><span class="page">page 16</span></footer>
</section>

<section class="slide process">
  <svg class="photo" width="816" height="458" viewBox="0 0 816 458" role="img" aria-label="Dark faceted background photo">
    <defs>
      <linearGradient id="darkWedge" x1="0" y1="0" x2="0" y2="1">
        <stop offset="0" stop-color="#5b6b9c"/>
        <stop offset=".5" stop-color="#3a4058"/>
        <stop offset="1" stop-color="#1a1c24"/>
      </linearGradient>
    </defs>
    <polygon points="625,0 816,0 816,458 353,458" fill="url(#darkWedge)"/>
  </svg>
  <div class="step" style="top:52px">1</div>
  <div class="step" style="top:103px">2</div>
  <div class="step" style="top:155px">3</div>
  <div class="step" style="top:206px">4</div>
  <div class="step" style="top:257px">5</div>
  <div class="step" style="top:308px">6</div>
  <div class="step" style="top:360px">7</div>
  <p class="step-text left" style="top:45px">Work with our lender customers on their non-performing loan portfolio.</p>
  <p class="step-text right" style="top:105px">Purchase participation in non-performing loans.</p>
  <p class="step-text left" style="top:148px">Provide special servicing in compliance with bank's servicing criteria.</p>
  <p class="step-text right" style="top:212px">Provide bank access to NPL platform.</p>
  <p class="step-text left" style="top:250px">Maintain first right of refusal to purchase loan using proprietary algorithm.</p>
  <p class="step-text right" style="top:315px">Internal servicing standards.</p>
  <p class="step-text left" style="top:365px">Liquidation, when necessary.</p>
  <div class="section-card" role="img" aria-label="Faceted grey texture fading to blue">
    <span class="num heading">05</span>
    <span class="label heading">Our Process</span>
    <p class="desc">Initially partner with licensed collection agencies to supplement our in-house abilities (and comply with regulatory requirements). Potential to acquire and bring completely in-house.</p>
  </div>
  <footer class="footer"><span class="brand">Amber Heron</span><span class="rights">Not for distribution – All rights reserved © Amber Heron Fund</span><span class="page">page 17</span></footer>
</section>

<section class="slide customers">
  <h2 class="title heading">06-OUR CUSTOMERS</h2>
  <div class="skyline" role="img" aria-label="Hazy city skyline photo over water"></div>
  <div class="frame"></div>
  <span class="sub">Target Market</span>
  <div class="stat" style="left:329px"><div class="value">5000</div><div class="what">Community banks</div></div>
  <div class="stat" style="left:548px"><div class="value">4000</div><div class="what">Mid-Market banks</div></div>
  <footer class="footer"><span class="brand">Amber Heron</span><span class="rights">Not for distribution – All rights reserved © Amber Heron Fund</span><span class="page">page 18</span></footer>
</section>

</body>
</html>
```